Velmarone Website Redesign

We need a redesign of the company website.

We're a company, based in the UK, called Velmarone. We develop software for the Healthcare Industry, used by medical professionals throughout the UK on a daily basis.

We have a suite of tools that form the Velmarone Platform, and all are web-based.

We want to communicate that our software is not only innovative but is the best available, easy to use, and provides exceptional quality and RoI.

Additionally, we want our existing customers to be able to see what else we can offer them.

A site map is attached.
Updates

Hi Everyone,

As we approach the deadline for submissions, we’ve shortlisted threedesigns that we felt were the best of the submissions and have asked thedesigners to make some additional changes and produce some content pages so wecan see what’s beneath the Home page in the rest of the site.

Thank you all for your submissions – there was an awful lot ofdisagreement among everyone here over which designs we thought were best andsome of those that haven’t made it into the final three were very well liked.

Those in the final three have been messaged individually and have theirdesigns as the only non-eliminated ones showing. We would ask at this stagethat anyone not in the final three please do no further work or submitadditional designs as we are approaching the deadline and will not be able toprovide sufficient feedback to allow any changes in a short space of time.

Kind regards,
The Velmarone Team

Target Market(s)

Nurses and medical professionals in western-speaking countries, most notably in the UK.

Predominantly, we expect it will be senior medical staff that will be viewing (and using) our website - some will be existing customers and some will be new or potential customers.

Industry/Entity Type

Medical

Requirements
Must have
• Area to showcase and provide information about products.
• Company information - who we are and why you should choose us.
• News and events - blog, archive newsletters, publications, etc.
• Support section for existing customers - FAQ, Forum, Manuals.
• Contact page.
• We also feel that we'd like to have our telephone number and primary email address visible at all times, with an immediate ability for users to request a demonstration.
Nice to have
• A "My Velmarone" area would be nice at some point, though that's something for further down the line.

```html
<!DOCTYPE html>
<html lang="en">
<head>
<meta charset="utf-8">
<title>Velmarone Health</title>
<link href="https://fonts.googleapis.com/css2?family=Arimo:wght@400;700&family=PT+Sans:wght@400;700&family=Open+Sans:wght@400;600&display=swap" rel="stylesheet">
<style>
:root{
  --blue:#1a8ae6;
  --blue-dark:#0b5fc0;
  --link:#1a5fd6;
  --grey:#8a8a8a;
  --text:#333;
  --orange:#f26a1b;
  --green-band:#cdeecf;
  --footer-top:#8c8c8c;
  --footer-bottom:#4a4a4a;
  --white:#fff;
}
*{box-sizing:border-box;margin:0;padding:0}
html,body{width:892px;height:1200px;overflow:hidden;background:var(--white)}
body{position:relative;font-family:"Arimo",Arial,sans-serif;color:var(--text)}
.abs{position:absolute}

/* header */
.brand{left:48px;top:30px;font-family:"Arimo",Arial,sans-serif;font-weight:700;font-size:42px;color:var(--blue);letter-spacing:-.5px}
.brand-rule{left:48px;top:81px;width:320px;height:3px;background:#9a9a9a}
.tagline{left:48px;top:88px;font-weight:700;font-size:18.5px;color:var(--grey)}
.search{left:716px;top:35px;width:158px;height:22px;border:1px solid #b8b8b8;border-radius:3px;font-size:12px;color:#a0a0a0;padding:3px 9px}
.search-icon{left:687px;top:32px}
.demo-btn{left:691px;top:79px;width:183px;height:32px;border-radius:3px;background:linear-gradient(#2f9bff,#0a5fe0);color:var(--white);font-weight:700;font-size:14.5px;text-align:center;line-height:32px;letter-spacing:.5px;box-shadow:0 2px 3px rgba(0,0,0,.3)}

/* navigation */
.nav{left:0;top:136px;width:892px;height:35px;background:linear-gradient(#f4f4f4,#c9c9c9);display:flex;border-top:1px solid #ddd}
.nav a{display:block;height:35px;line-height:35px;text-align:center;font-size:13.5px;color:#555;text-decoration:none;border-right:1px solid #aaa}
.nav a.active{background:linear-gradient(#fafafa,#e3e3e3);color:var(--blue)}
.subnav{left:0;top:173px;width:892px;height:20px;background:var(--green-band);display:flex;align-items:center;font-size:10.5px;color:#7a7a7a;padding-left:27px}
.subnav span{margin-right:18px;display:flex;align-items:center}
.subnav span.current{color:var(--blue)}
.subnav i{display:inline-block;width:5px;height:5px;background:#6cc0e0;margin-right:18px}

/* hero */
.hero{left:5px;top:196px;width:882px;height:212px;border-radius:12px;background:linear-gradient(90deg,#1f7fe0 0%,#6fb8f5 12%,#bfe2fb 30%,#6ab2f3 55%,#1b7ee6 88%,#1f7fe0 100%);overflow:hidden}
.hero-shade{left:0;top:0;width:882px;height:212px;background:linear-gradient(transparent 55%,rgba(255,255,255,.45))}
.hero-art{left:155px;top:9px;width:220px;height:190px;border-radius:4px;background:linear-gradient(135deg,#6d63d9,#f2c41e 70%,#e8522a)}
.hero-title{left:423px;top:42px;font-family:"PT Sans",sans-serif;font-size:38px;color:var(--white);letter-spacing:.5px}
.hero-copy{left:424px;top:86px;width:340px;font-family:"Open Sans",sans-serif;font-weight:600;font-size:12.8px;line-height:16px;color:#111}
.hero-arrow{top:82px}

/* main column */
.h2{font-family:"PT Sans",sans-serif;font-size:24px;color:var(--blue);font-weight:400}
.copy{font-family:"Open Sans",sans-serif;font-size:11px;line-height:13.5px;color:#222;text-align:justify}
.copy p{text-indent:10px;margin-bottom:13px}
.copy p + p{text-indent:36px}
.read-more{font-size:11px;color:var(--blue)}
.photo{border:1px solid #ddd}
.news-list{left:260px;top:692px;width:310px;list-style:none;font-size:11.5px;line-height:13.5px}
.news-list li{position:relative;padding-left:19px;margin-bottom:15px}
.news-list li::before{content:"";position:absolute;left:0;top:4px;width:7px;height:7px;background:var(--link)}
.news-list a{color:var(--link)}
.blog-title{left:42px;top:875px;font-family:"PT Sans",sans-serif;font-size:23px;color:var(--orange)}
.rss{left:405px;top:916px;width:112px;height:110px;border-radius:18px;background:linear-gradient(135deg,#ff8a3a,#e34f0c)}
.blog-band{left:37px;top:1054px;width:541px;height:21px;background:#e3f6f8;text-align:right;padding-right:26px;font-size:11px;line-height:21px;color:var(--orange)}

/* side panels */
.panel{border-radius:14px;border:2px solid #e6eef6;box-shadow:0 0 3px rgba(0,0,0,.15)}
.login{left:610px;top:430px;width:257px;height:265px;background:linear-gradient(#fbfdff,#d6e9fb 45%,#5b9ff0)}
.login-title{left:32px;top:10px;font-family:"PT Sans",sans-serif;font-size:28px;color:var(--blue)}
.login-rule{left:30px;top:48px;width:210px;height:1px;background:#8a9bb0}
.logged{left:17px;top:63px;font-size:12.5px;color:#444}
.logged b{color:var(--orange);font-weight:400}
.label{left:20px;font-size:10.5px;color:#444}
.field{left:20px;width:217px;height:19px;background:#f0f2f4;border:1px solid #d5dce3;border-radius:2px;font-size:9px;color:#aaa;padding-left:6px;line-height:17px;letter-spacing:1px}
.remember{left:23px;top:183px;font-size:9.5px;color:#444;display:flex;align-items:center}
.remember i{width:12px;height:12px;border:1px solid #5aa;background:#d7f3f3;margin-right:6px}
.remember b{color:var(--orange);font-weight:400;margin-left:3px}
.login-btn{left:162px;top:202px;width:75px;height:24px;border-radius:6px;background:linear-gradient(#f4f4f4,#c4c4c4);border:1px solid #999;text-align:center;font-size:13px;line-height:22px;color:#333}
.small-links{left:24px;top:216px;font-size:9px;line-height:12px;color:#333;text-decoration:underline}
.newsletter{left:610px;top:705px;width:256px;height:75px;border-radius:6px;background:linear-gradient(#e8f8e2,#6fd050 75%,#4dbb33)}
.newsletter h3{position:absolute;left:18px;top:8px;font-family:"PT Sans",sans-serif;font-weight:400;font-size:21px;color:#444}
.nl-input{left:20px;top:42px;width:145px;height:21px;background:#eef1ee;border-radius:3px 0 0 3px;font-size:9px;color:#999;line-height:21px;padding-left:12px}
.nl-btn{left:163px;top:41px;width:75px;height:23px;border-radius:4px;background:linear-gradient(#f4f4f4,#c6c6c6);border:1px solid #999;font-size:12.5px;text-align:center;line-height:21px;color:#333}
.testimonials{left:610px;top:793px;width:257px;height:282px;background:linear-gradient(#fcfdff,#dff1d4 40%,#7dd25a)}
.testimonials h3{position:absolute;left:25px;top:12px;font-family:"PT Sans",sans-serif;font-weight:400;font-size:20px;color:var(--blue)}
.quote{left:25px;width:220px;font-family:"PT Sans",sans-serif;font-size:14px;line-height:20px;color:#333}
.quote cite{display:block;text-align:right;font-style:normal;color:var(--blue-dark);padding-right:0}

/* footer */
.footer{left:5px;top:1085px;width:882px;height:110px;background:linear-gradient(var(--footer-top),var(--footer-bottom))}
.contact{left:19px;top:15px;font-size:12.5px;line-height:16px;color:#eee}
.contact strong{color:var(--white)}
.hotline{left:410px;top:22px;font-family:"PT Sans",sans-serif;font-size:29px;line-height:33px;color:var(--white)}
.hotline span{color:#f7a21b}
</style>
</head>
<body>

<header>
  <div class="abs brand">Velmarone Health</div>
  <div class="abs brand-rule"></div>
  <div class="abs tagline">Bringing Technology to Healthcare</div>
  <svg class="abs search-icon" width="30" height="30" viewBox="0 0 30 30" aria-hidden="true">
    <circle cx="12" cy="12" r="9" fill="#eef4fb" stroke="#7a8ea8" stroke-width="2.5"/>
    <line x1="18.5" y1="18.5" x2="27" y2="27" stroke="#4d5f78" stroke-width="4" stroke-linecap="round"/>
  </svg>
  <div class="abs search">Search Velmarone</div>
  <div class="abs demo-btn">REQUEST A DEMO</div>
</header>

<nav class="abs nav">
  <a style="width:98px">Home</a>
  <a style="width:158px">Products &amp; Services</a>
  <a class="active" style="width:138px">About Velmarone</a>
  <a style="width:149px">News and Events</a>
  <a style="width:97px">Support</a>
  <a style="width:119px">Contact us</a>
  <a style="width:133px;border-right:0">My Velmarone</a>
</nav>
<div class="abs subnav">
  <span class="current">About Velmarone</span><i></i>
  <span>Leadership Team</span><i></i>
  <span>Advisory Board</span><i></i>
  <span>Partnerships</span><i></i>
  <span>Experienced Clinical Staff</span><i></i>
  <span>Medical Solutions Architects</span><i></i>
  <span>Clients List</span>
</div>

<section class="abs hero">
  <div class="abs hero-shade"></div>
  <div class="abs hero-art" role="img" aria-label="Two boxed software product packages"></div>
  <svg class="abs hero-arrow" style="left:16px" width="40" height="40" viewBox="0 0 40 40" aria-hidden="true">
    <circle cx="20" cy="20" r="16" fill="none" stroke="#c9d3de" stroke-width="4"/>
    <path d="M23 11 L14 20 L23 29" fill="none" stroke="#c9d3de" stroke-width="4"/>
  </svg>
  <svg class="abs hero-arrow" style="left:823px" width="40" height="40" viewBox="0 0 40 40" aria-hidden="true">
    <circle cx="20" cy="20" r="16" fill="none" stroke="#c9d3de" stroke-width="4"/>
    <path d="M17 11 L26 20 L17 29" fill="none" stroke="#c9d3de" stroke-width="4"/>
  </svg>
  <svg class="abs" style="left:403px;top:24px" width="18" height="16" viewBox="0 0 18 16" aria-hidden="true">
    <path d="M0 16 H16 V0 L12 10 Z" fill="#fff"/>
  </svg>
  <div class="abs hero-title">PRODUCT SHOWCASE</div>
  <p class="abs hero-copy">We develop software for the Healthcare Industry, used by&nbsp; form the Velmarone Platform, and all are web-based.</p>
</section>

<main>
  <h2 class="abs h2" style="left:47px;top:439px">About Velmarone</h2>
  <div class="abs copy" style="left:47px;top:491px;width:243px">
    <p>In today's changing environment, healthcare organisations globally are faced with conflicting challenges; to reduce costs while offering improved healthcare services to patients that expect better and better services.</p>
    <p>Most health care organisations operate using either [rent technologies and systems that have been developed over a long period of time, ..........</p>
  </div>
  <div class="abs read-more" style="left:203px;top:621px">...... read more</div>
  <div class="abs photo" style="left:303px;top:471px;width:264px;height:154px;background:linear-gradient(90deg,#cfd6dc,#eef2f5 50%,#9fb5c8)" role="img" aria-label="Clinician seated at a desk with a medical imaging monitor"></div>

  <h2 class="abs h2" style="left:47px;top:655px">News and Events</h2>
  <div class="abs photo" style="left:35px;top:692px;width:203px;height:135px;background:linear-gradient(120deg,#e8eef2,#c9d8e4 55%,#8fa6b8)" role="img" aria-label="Two doctors reviewing information on a laptop"></div>
  <ul class="abs news-list">
    <li><a>Our New product launch in UK region. This weeks top Story. for more information click here .....</a></li>
    <li><a>Dr. Orlanda has invented new range of products&nbsp; for more information click here .....</a></li>
    <li><a>This years revolution in medical industry.</a></li>
  </ul>

  <h2 class="abs blog-title">VELMARONE NEWS BLOG</h2>
  <div class="abs copy" style="left:42px;top:911px;width:317px">
    <p>In today's changing environment, healthcare organisations globally are faced with conflicting challenges; to reduce costs while offering improved healthcare services to patients that expect better and better services.</p>
    <p>Most health care organisations operate using either manual paper based processed or a mix of different technologies and systems that have been developed over avices to patients that expect better and better services.</p>
  </div>
  <div class="abs rss" role="img" aria-label="Glossy orange news feed icon"></div>
  <div class="abs blog-band">...... read more</div>
</main>

<aside>
  <section class="abs panel login">
    <h3 class="abs login-title" style="font-weight:400">Login</h3>
    <div class="abs login-rule"></div>
    <p class="abs logged">You are logged in as <b>Sam Hollis</b></p>
    <div class="abs label" style="top:97px">E-mail ID / Login ID</div>
    <div class="abs field" style="top:111px"></div>
    <div class="abs label" style="top:132px">Password</div>
    <div class="abs field" style="top:147px">•••••••••••••••</div>
    <div class="abs remember"><i></i>Remember <b>Me</b></div>
    <div class="abs login-btn">Login</div>
    <div class="abs small-links">Forgot your password?<br>Sign up here</div>
  </section>

  <section class="abs newsletter">
    <h3>Subscribe for Newsletter</h3>
    <div class="abs nl-input">Enter your e-mail ID here</div>
    <div class="abs nl-btn">Subscribe</div>
  </section>

  <section class="abs panel testimonials">
    <h3>Customer Testimonials</h3>
    <blockquote class="abs quote" style="top:50px">Our organization using this product and it makes our lives easy.<cite>- Peter Anlow</cite></blockquote>
    <blockquote class="abs quote" style="top:130px">I am very happy that I have been using this wonderful product.<cite>- Martin Dael</cite></blockquote>
    <blockquote class="abs quote" style="top:202px">Our organization using this product and it makes our lives easy.<cite>- Peter Anlow</cite></blockquote>
  </section>
</aside>

<footer class="abs footer">
  <div class="abs contact">
    <strong>CONTACT INFORMATION</strong><br>
    Velmarone - # 48 Harrow Vale Road, London N9 4QT,<br>
    United Kingdom<br>
    Tel.: +44 (0) 208 555 0142&nbsp; +44 (0) 208 555 0142<br>
    <strong>Fax:</strong> +44 (0) 208 555 0187
  </div>
  <div class="abs hotline">
    <span>Call :</span> +44 (0) 208 555 0142<br>
    <span>E-Mail :</span> support@velmarone.com
  </div>
</footer>

</body>
</html>
```